Album Single Song Cover Art Needed - Hip-Hop, Pop, R&B Artist

Need a CD "Single Release" Cover Art designed for Native American Hip Hop Artist - K Lumina. Template: Pressvault - 300ppi. Two separate Art Designs - One with no wording; the other with Wording. Single Song Title is: Night Tide / Artist: K Lumina. Thoughts on artwork - Close Up of Face, create a vision of "Fierce". Looking to make a powerful statement - colors vibrant, splashy. Let your creativity run free - whatever "FIERCE" comes to mind, etc., Let me see what you can do. I provided a couple of pictures - take your pick of any to use - remove background. Happy designing!
Updates

Would like to see a few more designs come through as well as allow you to create additional designs. Thank you.

Target Market(s)

Music, Entertainment

Industry/Entity Type

Music, Entertainment

Font styles to use
Other font styles liked:
• Let the Designer Choose

Requirements
Must have
• FIERCE
Nice to have
• Vibrant, Color, Splashes - think "FIERCE"

```html
<!DOCTYPE html>
<html lang="en">
<head>
<meta charset="utf-8">
<title>K Lumina — Night Tide</title>
<link rel="stylesheet" href="https://fonts.googleapis.com/css2?family=Archivo+Black&family=Permanent+Marker&display=swap">
<style>
  :root {
    --bg-dark: #150609;
    --bg-green: #2fa77a;
    --bg-plum: #8a3a63;
    --bg-pink: #ff2a62;
    --portrait-yellow: #f4e21a;
    --portrait-red: #e8231c;
    --portrait-cyan: #3fd8e0;
    --portrait-blue: #1f3fb0;
    --title-white: #ffffff;
    --artist-ink: #111111;
  }
  html, body {
    margin: 0;
    padding: 0;
    width: 1200px;
    height: 1200px;
    overflow: hidden;
    background: var(--bg-dark);
  }
  .cover {
    position: relative;
    width: 1200px;
    height: 1200px;
    overflow: hidden;
    background:
      radial-gradient(ellipse 60% 45% at 15% 0%, rgba(47,167,122,0.9), rgba(47,167,122,0) 70%),
      radial-gradient(ellipse 70% 50% at 90% 0%, var(--bg-pink), rgba(255,42,98,0) 75%),
      linear-gradient(180deg, var(--bg-plum) 0%, #3a1424 25%, var(--bg-dark) 55%, var(--bg-dark) 100%);
  }
  .portrait {
    position: absolute;
    left: 0;
    top: 0;
    width: 1200px;
    height: 1200px;
  }
  .artist-name {
    position: absolute;
    top: 48px;
    left: 385px;
    margin: 0;
    font-family: "Archivo Black", sans-serif;
    font-size: 40px;
    letter-spacing: 24px;
    color: var(--title-white);
    -webkit-text-stroke: 2px var(--artist-ink);
    paint-order: stroke fill;
    text-shadow: 0 0 4px var(--artist-ink);
    text-transform: uppercase;
    white-space: nowrap;
  }
  .song-title {
    position: absolute;
    top: 1010px;
    left: 270px;
    margin: 0;
    font-family: "Permanent Marker", cursive;
    font-size: 120px;
    line-height: 1;
    color: var(--title-white);
    transform: skewX(-12deg);
    text-transform: uppercase;
    white-space: nowrap;
    text-shadow: 0 2px 6px rgba(0,0,0,0.35);
  }
</style>
</head>
<body>
  <main class="cover">
    <svg class="portrait" viewBox="0 0 1200 1200" role="img" aria-label="Vibrant pop-art close-up portrait of the artist in yellow, red, cyan and blue face paint with a head wrap">
      <defs>
        <radialGradient id="portraitTone" cx="65%" cy="45%" r="60%">
          <stop offset="0%" stop-color="#fff8a0"/>
          <stop offset="35%" stop-color="#f4e21a"/>
          <stop offset="65%" stop-color="#e8231c"/>
          <stop offset="85%" stop-color="#3fd8e0"/>
          <stop offset="100%" stop-color="#1f3fb0"/>
        </radialGradient>
      </defs>
      <path d="M330 90 C420 40 600 20 800 30 C1000 40 1200 150 1200 300 L1200 1200 L130 1200 C200 1150 330 1080 560 1040 C520 900 500 700 520 560 C420 520 330 420 330 300 Z" fill="url(#portraitTone)"/>
    </svg>
    <h1 class="artist-name">K Lumina</h1>
    <h2 class="song-title">Night Tide</h2>
  </main>
</body>
</html>
```